Come Play With Us!!! We are the Elite

We need a hiring flyer to hand out to potential recruits.
Please promote our social pages.
Something attractive, and informative with calls to action to contact us.
Please promote for people to follow us on social media.
We would like to list the following advantages to work here:
• Industry Leading Compensation
• Structured Career Advancement
• Safe Work Environment
• Work Promise Policy (Full Time Staff)
• Health & Dental Benefits
• Paid Training Programs
• Paid Clothing Allowance
• Paid Boot Allowance
• Positive Culture
• Progressive Culture
• Equal Opportunity Employer
• Veteran Friendly Employer
• New Equipment
• Paid Leadership Training
• Transparent Communication
• Community Focused
• Prestigious Clientele
• Local Work
• Focused on using industry leading tech
• Tool Purchase Program
• Family Atmosphere
• Team Events (Sports games, Lunches, Get togethers, Etc)
• Work Life balance
• Daily On Call Snow Pay
- Sick Pay
- Positive reputation
• Bonus’s available:
o Winter Shift Premium
o Referral Bonus
o Project Incentives
Current Positions open:
- Winter Crew Members
- Salt Truck Driver/Operator (AZ/DZ/AR)
- Winter Equipment Operators
- Construction Foreperson
Landscape and Construction

```html
<!DOCTYPE html>
<html lang="en">
<head>
<meta charset="utf-8">
<title>Ridgeline Contracting Group – We Are Hiring</title>
<link href="https://fonts.googleapis.com/css2?family=League+Gothic&family=Montserrat:wght@300;400;700&display=swap" rel="stylesheet">
<style>
  :root{
    --backdrop:#5e5e5e;
    --paper:#ffffff;
    --strip:#e9e9ea;
    --green-bright:#8dc63f;
    --green-mid:#4fae4a;
    --green-deep:#1d8f41;
    --green-dark:#0b8449;
    --charcoal:#4a4a4c;
    --ink:#3d3d3f;
    --bullet:#9b9b9d;
    --white:#ffffff;
  }
  *{margin:0;padding:0;box-sizing:border-box}
  html,body{width:1200px;height:1200px;overflow:hidden;background:var(--backdrop)}
  .flyer{position:absolute;left:176px;top:0;width:848px;height:1200px;background:var(--strip);overflow:hidden;font-family:"Montserrat",sans-serif}
  .photo{position:absolute;left:0;top:21px;width:848px;height:505px;
    background:linear-gradient(100deg,#cdbfa8 0%,#bfae93 35%,#8f8a80 55%,#3a3d4a 75%,#23263a 100%)}
  .brand-box{position:absolute;left:50px;top:21px;width:285px;height:252px;
    background:linear-gradient(180deg,#ececed 0%,#ffffff 60%);display:flex;align-items:center;justify-content:center;gap:12px;padding-top:60px}
  .brand-mark{width:40px;height:40px;border-radius:50%;background:var(--green-deep);flex:none}
  .brand-name{font-family:"Montserrat",sans-serif;font-weight:400;font-size:19px;line-height:1.15;letter-spacing:1.5px;color:var(--ink)}
  .hire-band{position:absolute;left:0;top:526px;width:848px;height:317px;
    background:linear-gradient(180deg,var(--green-mid) 0%,var(--green-deep) 100%)}
  .headline{position:absolute;left:68px;font-family:"League Gothic",sans-serif;line-height:1;text-transform:uppercase}
  .headline--outline{top:562px;font-size:70px;color:transparent;-webkit-text-stroke:1.6px var(--white);letter-spacing:1px}
  .headline--solid{top:632px;font-size:146px;color:var(--white);letter-spacing:-1px}
  .headline--tag{top:755px;font-size:48px;color:var(--green-bright)}
  .positions-head{position:absolute;left:422px;top:494px;width:354px;height:103px;background:var(--green-dark);
    font-family:"League Gothic",sans-serif;font-size:44px;color:var(--white);text-align:center;line-height:103px;letter-spacing:.5px}
  .positions-notch{position:absolute;left:588px;top:596px}
  .positions-list{position:absolute;left:422px;top:597px;width:354px;height:277px;background:var(--green-bright);list-style:none;padding:48px 0 0 41px}
  .positions-list li{position:relative;padding-left:20px;font-family:"League Gothic",sans-serif;font-size:28px;line-height:26px;color:var(--white);margin-bottom:14px}
  .positions-list li::before{content:"";position:absolute;left:0;top:6px;border-left:11px solid var(--white);border-top:7px solid transparent;border-bottom:7px solid transparent}
  .benefits-panel{position:absolute;left:0;top:843px;width:848px;height:231px;background:var(--charcoal)}
  .benefits-pill{position:absolute;left:68px;top:823px;width:149px;height:39px;border-radius:20px;background:var(--white);
    font-weight:700;font-size:18px;color:var(--charcoal);text-align:center;line-height:39px;letter-spacing:-.5px}
  .benefits-text{position:absolute;left:68px;top:872px;width:740px;font-weight:300;font-size:14.4px;line-height:17.6px;color:var(--white);letter-spacing:-.25px}
  .benefits-text .perk{white-space:nowrap}
  .benefits-text .perk--accent{color:var(--green-bright)}
  .benefits-text .dot{display:inline-block;width:6px;height:6px;border-radius:50%;background:var(--bullet);margin:0 5px 2px 0;vertical-align:middle}
  .contact-bar{position:absolute;left:0;top:1074px;width:848px;height:126px;background:linear-gradient(180deg,#dededf 0%,#f6f6f6 30%,#ffffff 100%)}
  .contact{position:absolute;display:flex;align-items:center;gap:6px;font-weight:400;font-size:14px;color:#58585a}
  .contact .chip{width:35px;height:35px;border-radius:4px;background:#5a5a5c;display:flex;align-items:center;justify-content:center;flex:none}
</style>
</head>
<body>
<main class="flyer">
  <div class="photo" role="img" aria-label="Photo of a smiling crew member in a cap holding a cordless drill on a sandy construction site, a coworker in a safety vest kneeling in the background"></div>

  <div class="brand-box">
    <span class="brand-mark"></span>
    <span class="brand-name">RIDGELINE<br>CONTRACTING<br>GROUP</span>
  </div>

  <section class="hire-band"></section>
  <h1 class="headline headline--outline">We Are</h1>
  <div class="headline headline--solid">Hiring!</div>
  <div class="headline headline--tag">Come Play With Us!!!</div>

  <div class="positions-head">POSITIONS AVAILABLE</div>
  <ul class="positions-list">
    <li>WINTER CREW MEMBERS</li>
    <li>SALT TRUCK DRIVER / OPERATOR<br>( AZ / DZ / AR )</li>
    <li>WINTER EQUIPMENT OPERATORS</li>
    <li>CONSTRUCTION FOREPERSON</li>
  </ul>
  <svg class="positions-notch" width="34" height="22" viewBox="0 0 34 22"><polygon points="0,0 34,0 17,19" fill="#0b8449"/></svg>

  <section class="benefits-panel"></section>
  <div class="benefits-pill">BENEFITS</div>
  <p class="benefits-text">
    <span class="perk perk--accent"><span class="dot"></span>Industry Leading Compensation</span><br>
    <span class="perk"><span class="dot"></span>Structured Career Advancement</span> <span class="perk perk--accent"><span class="dot"></span>Safe Work Environment</span> <span class="perk"><span class="dot"></span>Work Promise Policy (Full Time Staff)</span><br>
    <span class="perk perk--accent"><span class="dot"></span>Health &amp; Dental Benefits</span> <span class="perk"><span class="dot"></span>Paid Training Programs</span> <span class="perk perk--accent"><span class="dot"></span>Paid Clothing Allowance</span><br>
    <span class="perk"><span class="dot"></span>Paid Boot Allowance</span> <span class="perk perk--accent"><span class="dot"></span>Positive Culture</span> <span class="perk"><span class="dot"></span>Progressive Culture</span> <span class="perk perk--accent"><span class="dot"></span>Equal Opportunity Employer</span><br>
    <span class="perk"><span class="dot"></span>Veteran Friendly Employer</span> <span class="perk perk--accent"><span class="dot"></span>New Equipment</span> <span class="perk"><span class="dot"></span>Paid Leadership Training</span><br>
    <span class="perk perk--accent"><span class="dot"></span>Transparent Communication</span> <span class="perk"><span class="dot"></span>Community Focused</span> <span class="perk perk--accent"><span class="dot"></span>Prestigious Clientele</span> <span class="perk"><span class="dot"></span>Local Work</span><br>
    <span class="perk perk--accent"><span class="dot"></span>Focused on using industry leading tech</span> <span class="perk"><span class="dot"></span>Tool Purchase Program</span> <span class="perk perk--accent"><span class="dot"></span>Family Atmosphere</span><br>
    <span class="perk"><span class="dot"></span>Team Events (Sports games, Lunches, Get togethers, Etc)</span> <span class="perk perk--accent"><span class="dot"></span>Work Life balance</span><br>
    <span class="perk"><span class="dot"></span>Daily On Call Snow Pay (Sick Pay, Positive reputation)</span><br>
    <span class="perk perk--accent"><span class="dot"></span>Bonus’s available (Winter Shift Premium, Referral Bonus, Project Incentives)</span>
  </p>

  <footer class="contact-bar"></footer>
  <div class="contact" style="left:68px;top:1100px">
    <span class="chip"><svg width="22" height="22" viewBox="0 0 22 22" fill="none" stroke="#fff" stroke-width="1.4"><circle cx="11" cy="11" r="9"/><ellipse cx="11" cy="11" rx="4" ry="9"/><line x1="2" y1="11" x2="20" y2="11"/><line x1="3.5" y1="6.5" x2="18.5" y2="6.5"/><line x1="3.5" y1="15.5" x2="18.5" y2="15.5"/></svg></span>
    www.ridgelinecontracting.com
  </div>
  <div class="contact" style="left:68px;top:1139px">
    <span class="chip"><svg width="20" height="20" viewBox="0 0 24 24"><path fill="#fff" d="M6.6 10.8a15 15 0 0 0 6.6 6.6l2.2-2.2c.3-.3.7-.4 1-.2 1.1.4 2.3.6 3.6.6.6 0 1 .4 1 1V20c0 .6-.4 1-1 1A17 17 0 0 1 3 4c0-.6.4-1 1-1h3.5c.6 0 1 .4 1 1 0 1.3.2 2.5.6 3.6.1.3 0 .7-.2 1z"/></svg></span>
    555-014-2290
  </div>
  <div class="contact" style="left:430px;top:1100px"><span class="chip"></span>ridgelinecontracting</div>
  <div class="contact" style="left:627px;top:1100px"><span class="chip"></span>RContractingInc</div>
  <div class="contact" style="left:430px;top:1139px"><span class="chip"></span>ridgeline_contracting</div>
</main>
</body>
</html>
```